Single Graphic Re-Design on Website Homepage

We have this portion of an upcoming website that we want help designing better. Basically our platform allows a user to submit one loan app and it will go to various competing lenders to obtain this best terms possible. So some sort of graphic that displays it's function. Possibly sitting at a computer, or sending a loan app details and shooting out to 4-5 lenders. We want to keep the colors the same as the website, the BETA link can be found here, where the graphic which will be created will replace. https://bluecanter.vostelink.net/ To be Clear, it is just the section that states "Submit A Loan Request" This is the section i am struggling with the most to come up with an amazing design.

Target Market(s)

Investors, Entreupenuers, Generally men aged 30-45

Industry/Entity Type

Loans and mortgages

Colors
0054AA
0677BA
7BADD7
CADEEF
E8F1F8
F0912C
F2A743
F7CA91
FBE8D2
FDF5EE

Requirements
Must have
• Same Aesthetic feel as current site (see test link)
Nice to have
• A graphic that shows the loan request being placed and "shot out" to multiple lenders
Should not have
• Differnt colors to existing site, differnt aesthetic feel.

```html
<!DOCTYPE html>
<html lang="en">
<head>
<meta charset="utf-8">
<title>Lendvane.com – Home</title>
<link href="https://fonts.googleapis.com/css2?family=Inter:wght@300;400;500;600;700&display=swap" rel="stylesheet">
<style>
:root{
  --navy:#1f5a8c;
  --navy-deep:#1e4f80;
  --band-blue:#3d5a8a;
  --ach-blue:#1e5a86;
  --orange:#f0912c;
  --orange-mid:#f2a743;
  --orange-soft:#f7ca91;
  --orange-pale:#fbe8d2;
  --sky:#cadeef;
  --sky-pale:#e8f1f8;
  --map:#6b94bd;
  --pale:#f3f6f9;
  --card-bg:#e8eef3;
  --ink:#222831;
  --muted:#5b6470;
  --white:#ffffff;
}
*{box-sizing:border-box;margin:0;padding:0}
html,body{width:1200px;height:3125px;overflow:hidden}
body{position:relative;font-family:"Inter",sans-serif;color:var(--ink);background:var(--white)}
.abs{position:absolute}
.accent{color:var(--orange)}

/* header */
.site-header{left:0;top:0;width:1200px;height:67px;background:var(--white);border-bottom:1px solid #e6e9ee}
.brand{left:102px;top:22px;font-size:19px;font-weight:600;color:var(--navy-deep);display:flex;align-items:center;gap:8px}
.brand-dot{width:12px;height:12px;border-radius:50%;background:var(--orange)}
.nav-link{top:26px;font-size:13px;font-weight:500;color:var(--navy-deep)}
.btn-signup{left:912px;top:21px;width:78px;height:27px;border-radius:14px;background:var(--navy-deep);color:#fff;font-size:13px;font-weight:600;display:flex;align-items:center;justify-content:center}
.btn-login{left:1006px;top:21px;width:92px;height:27px;border-radius:14px;border:1px solid var(--navy-deep);color:var(--navy-deep);font-size:13px;display:flex;align-items:center;justify-content:center;gap:6px}

/* shared */
.h-bold{font-weight:700;color:var(--navy);font-size:37px;letter-spacing:-.3px}
.h-light{font-weight:400;color:var(--navy);font-size:32px;line-height:36px}
.body-text{font-size:16px;line-height:25px;color:var(--ink)}
.body-text p+p{margin-top:12px}
.btn-framed{background:var(--navy-deep);color:#fff;font-size:13.5px;font-weight:500;display:flex;align-items:center;justify-content:center;outline:1px dashed rgba(255,255,255,.7);outline-offset:-5px}

/* hero */
.hero{left:0;top:67px;width:1200px;height:506px;background:var(--pale)}
.map-art{left:534px;top:146px;width:558px;height:351px;background:var(--map);border-radius:40px 60px 90px 40px}

/* videos */
.video{border-radius:10px;overflow:hidden;box-shadow:0 6px 16px rgba(0,0,0,.18)}
.video-bg{position:absolute;inset:0}
.video-bar{position:absolute;left:0;top:0;right:0;height:56px;display:flex;align-items:center;padding:0 12px;gap:10px;color:#fff;font-size:14px}
.avatar{width:27px;height:27px;border-radius:50%;background:#5a6fd6}
.video-act{position:absolute;top:14px;color:#fff;font-size:11px;text-align:center;display:flex;flex-direction:column;align-items:center;gap:4px}

/* loan section */
.loan-band{left:0;top:1032px;width:1200px;height:446px;background:var(--pale)}
.loan-flow{left:672px;top:1040px;width:440px;height:320px}
.partner{top:1398px;height:36px;width:62px;border-radius:18px;background:#d6e2ee}

/* cma */
.cma-card{left:102px;top:1991px;width:996px;height:330px;background:var(--card-bg);border-radius:22px}
.cma-inner{left:133px;top:2018px;width:933px;height:278px;border:1.5px dashed #3b4450;border-radius:22px;text-align:center}
.btn-outline{left:531px;top:2213px;width:136px;height:42px;border:1px solid var(--navy-deep);border-radius:22px;color:var(--navy-deep);font-size:13px;display:flex;align-items:center;justify-content:center;gap:8px}

/* calculators */
.calc-glow{left:360px;top:2425px;width:480px;height:480px;border-radius:50%;background:radial-gradient(circle,#fdf5ee 0%,#f6f8fb 60%,rgba(255,255,255,0) 72%)}
.calc-card{width:316px;height:139px;border-radius:16px;background:#f7f7f7;box-shadow:0 3px 10px rgba(0,0,0,.08);display:flex;flex-direction:column;align-items:center;justify-content:center;gap:18px;color:var(--navy);font-size:17.5px;font-weight:500}
.calc-art{left:800px;top:2487px;width:255px;height:279px;border-radius:8px;background:linear-gradient(170deg,#fbe8d2 0%,#f0912c 50%,#1f5a8c 100%)}

/* achievements */
.ach-band{left:0;top:2942px;width:1200px;height:183px;background:var(--pale)}
.ach-box{left:90px;top:2912px;width:1020px;height:203px;background:var(--ach-blue);border-radius:16px;overflow:hidden}
.ach-ring{left:106px;top:2929px;width:128px;height:128px;border-radius:50%;background:rgba(255,255,255,.06)}
.medal{left:168px;top:2960px;width:38px;height:38px;border-radius:50%;background:#f2a743}
.ach-title{left:223px;top:2993px;color:#fff;font-size:27px;font-weight:700}
.stat{width:180px;text-align:center;color:#fff}
.stat-num{font-size:27px;font-weight:700;margin-top:6px}
.stat-label{font-size:13px;margin-top:6px}
</style>
</head>
<body>

<header class="abs site-header">
  <div class="abs brand"><span>Lendvane.com</span><span class="brand-dot"></span></div>
  <span class="abs nav-link" style="left:649px">Calculator Estimator ⌄</span>
  <span class="abs nav-link" style="left:798px">Contact us</span>
  <div class="abs btn-signup">Sign up</div>
  <div class="abs btn-login">Log in
    <svg width="13" height="13" viewBox="0 0 14 14" fill="none" stroke="currentColor" stroke-width="1.4"><circle cx="7" cy="4.5" r="3"/><path d="M1.5 13c.6-3 2.8-4.5 5.5-4.5s4.9 1.5 5.5 4.5"/></svg>
  </div>
</header>

<!-- Browse lenders -->
<section class="abs hero"></section>
<h1 class="abs h-bold" style="left:102px;top:170px">Browse <span class="accent">Lenders</span></h1>
<div class="abs body-text" style="left:102px;top:228px;width:412px">Easily search for verified private lending companies by selecting your local market. Browse detailed lender profiles, review their loan terms, and connect directly to discuss your project. Whether you're funding a fix-and-flip, rental, or new construction, Lendvane.com makes it simple to find the right capital partner for your next investment.</div>
<div class="abs btn-framed" style="left:98px;top:437px;width:143px;height:46px">Select the State</div>
<svg class="abs" style="left:245px;top:415px" width="250" height="75" viewBox="0 0 250 75" fill="none" stroke="var(--navy-deep)" stroke-width="1.5" stroke-dasharray="3 4">
  <path d="M5 40c30 14 70 12 80-10s-20-30-20-5 40 40 90 5 50-20 85-25"/>
</svg>
<svg class="abs" style="left:477px;top:418px" width="14" height="14" viewBox="0 0 14 14"><path d="M0 2l14 3-9 9z" fill="var(--navy-deep)"/></svg>
<div class="abs map-art" role="img" aria-label="Map of the United States with state abbreviations"></div>

<!-- Platform video -->
<div class="abs" style="left:0;top:609px;width:456px;height:388px;background:var(--band-blue)"></div>
<div class="abs video" style="left:101px;top:671px;width:468px;height:263px">
  <div class="video-bg" role="img" aria-label="Video still of a presenter explaining how to use the platform" style="background:linear-gradient(135deg,#3a3530 0%,#6e6258 50%,#1e1b19 100%)"></div>
  <div class="video-bar"><span class="avatar"></span><span>Lendvane - How To Use</span></div>
  <div class="video-act" style="left:342px">◷<span>Watch later</span></div>
  <div class="video-act" style="left:417px">↪<span>Share</span></div>
</div>
<h2 class="abs h-light" style="left:625px;top:684px;width:470px">The go-to platform for real estate investors and <span class="accent">brokers to access private capital.</span></h2>
<div class="abs body-text" style="left:625px;top:798px;width:475px"><p>Our platform makes it easy for borrowers to submit loan requests and connect directly with lenders.</p><p>Discover trusted service providers and explore a wide range of free tools and education.</p></div>

<!-- Submit loan request -->
<section class="abs loan-band"></section>
<h2 class="abs h-bold" style="left:84px;top:1093px">Submit a <span class="accent">Loan Request</span></h2>
<div class="abs body-text" style="left:84px;top:1152px;width:498px;line-height:26.7px"><p>If you have a deal ready to go and need quick financing, simply submit a loan request below. Multiple lenders will review your property details and background, then submit their term sheets — giving you full control to choose the best lending partner for your needs.</p><p>Having the right lender on your team isn't just helpful — it's essential to your success.</p></div>
<div class="abs btn-framed" style="left:80px;top:1386px;width:170px;height:44px">Apply Loan Request</div>
<svg class="abs" style="left:268px;top:1360px" width="400" height="70" viewBox="0 0 400 70" fill="none" stroke="var(--navy-deep)" stroke-width="1.5" stroke-dasharray="4 4">
  <path d="M2 45c90 20 230 22 290 0s20-45-10-25 30 55 110 0"/>
</svg>
<svg class="abs" style="left:650px;top:1385px" width="14" height="14" viewBox="0 0 14 14"><path d="M0 2l14-2-5 13z" fill="var(--navy-deep)"/></svg>

<svg class="abs loan-flow" viewBox="0 0 440 320" role="img" aria-label="One loan request card sent out to five competing lenders, each returning a term sheet" font-family="Inter, sans-serif">
  <defs>
    <marker id="arrow-head" viewBox="0 0 10 10" refX="8" refY="5" markerWidth="7" markerHeight="7" orient="auto"><path d="M0 0L10 5 0 10z" fill="#f0912c"/></marker>
  </defs>
  <circle cx="150" cy="160" r="120" fill="#e8f1f8"/>
  <!-- request card -->
  <rect x="8" y="58" width="160" height="206" rx="12" fill="#fff" stroke="#cadeef" stroke-width="1.5"/>
  <path d="M8 70a12 12 0 0112-12h136a12 12 0 0112 12v26H8z" fill="#f0912c"/>
  <text x="24" y="82" fill="#fff" font-size="13" font-weight="700">Loan Request</text>
  <g font-size="11">
    <text x="24" y="120" fill="#5b6470">Property</text><text x="152" y="120" fill="#1f5a8c" font-weight="600" text-anchor="end">Fix &amp; Flip</text>
    <line x1="24" y1="130" x2="152" y2="130" stroke="#e8f1f8"/>
    <text x="24" y="148" fill="#5b6470">Amount</text><text x="152" y="148" fill="#1f5a8c" font-weight="600" text-anchor="end">$420,000</text>
    <line x1="24" y1="158" x2="152" y2="158" stroke="#e8f1f8"/>
    <text x="24" y="176" fill="#5b6470">LTV</text><text x="152" y="176" fill="#1f5a8c" font-weight="600" text-anchor="end">70%</text>
    <line x1="24" y1="186" x2="152" y2="186" stroke="#e8f1f8"/>
    <text x="24" y="204" fill="#5b6470">Term</text><text x="152" y="204" fill="#1f5a8c" font-weight="600" text-anchor="end">12 months</text>
  </g>
  <rect x="24" y="222" width="128" height="28" rx="6" fill="#1e4f80"/>
  <text x="88" y="240" fill="#fff" font-size="11.5" font-weight="600" text-anchor="middle">Submit ➤</text>
  <!-- arrows -->
  <g fill="none" stroke="#f0912c" stroke-width="1.6" stroke-dasharray="4 4" marker-end="url(#arrow-head)">
    <path d="M170 160C210 160 220 34 272 34"/>
    <path d="M170 160C215 160 225 97 272 97"/>
    <path d="M170 160H272"/>
    <path d="M170 160C215 160 225 223 272 223"/>
    <path d="M170 160C210 160 220 286 272 286"/>
  </g>
  <circle cx="170" cy="160" r="5" fill="#f0912c"/>
  <!-- lenders -->
  <g font-size="11.5">
    <g transform="translate(276 12)"><rect width="156" height="44" rx="10" fill="#fff" stroke="#cadeef"/><circle cx="22" cy="22" r="11" fill="#1f5a8c"/><text x="42" y="19" fill="#1f5a8c" font-weight="700">Lender A</text><text x="42" y="34" fill="#f0912c" font-size="10">Term sheet ✓</text></g>
    <g transform="translate(276 75)"><rect width="156" height="44" rx="10" fill="#fff" stroke="#cadeef"/><circle cx="22" cy="22" r="11" fill="#0677ba"/><text x="42" y="19" fill="#1f5a8c" font-weight="700">Lender B</text><text x="42" y="34" fill="#f0912c" font-size="10">Term sheet ✓</text></g>
    <g transform="translate(276 138)"><rect width="156" height="44" rx="10" fill="#fbe8d2" stroke="#f0912c"/><circle cx="22" cy="22" r="11" fill="#f0912c"/><text x="42" y="19" fill="#1f5a8c" font-weight="700">Lender C</text><text x="42" y="34" fill="#f0912c" font-size="10">Best terms ★</text></g>
    <g transform="translate(276 201)"><rect width="156" height="44" rx="10" fill="#fff" stroke="#cadeef"/><circle cx="22" cy="22" r="11" fill="#7badd7"/><text x="42" y="19" fill="#1f5a8c" font-weight="700">Lender D</text><text x="42" y="34" fill="#f0912c" font-size="10">Term sheet ✓</text></g>
    <g transform="translate(276 264)"><rect width="156" height="44" rx="10" fill="#fff" stroke="#cadeef"/><circle cx="22" cy="22" r="11" fill="#1e4f80"/><text x="42" y="19" fill="#1f5a8c" font-weight="700">Lender E</text><text x="42" y="34" fill="#f0912c" font-size="10">Term sheet ✓</text></g>
  </g>
</svg>

<div class="abs partner" style="left:688px"></div>
<div class="abs partner" style="left:764px"></div>
<div class="abs partner" style="left:840px"></div>
<div class="abs partner" style="left:916px"></div>
<div class="abs partner" style="left:992px"></div>
<div class="abs partner" style="left:1100px"></div>

<!-- Free tools -->
<div class="abs" style="left:744px;top:1514px;width:456px;height:430px;background:var(--band-blue)"></div>
<h2 class="abs h-light" style="left:102px;top:1576px">Free tools at <span class="accent">Lendvane.</span></h2>
<div class="abs body-text" style="left:102px;top:1620px;width:478px"><p>Use our free tools at Lendvane to make smarter decisions and move through your investment journey with confidence.</p><p>At Lendvane, our mission is to provide real estate investors with everything they need to make smart, informed decisions — whether purchasing, refinancing, or scaling their portfolio.</p><p>From powerful calculators and free comparable reports to insurance quotes, investment property listings, and educational resources, we're here to reduce your costs, increase your confidence, and simplify every step of your investment journey.</p></div>
<div class="abs video" style="left:615px;top:1598px;width:468px;height:263px">
  <div class="video-bg" role="img" aria-label="Video still of a presenter announcing new calculators and tools" style="background:linear-gradient(135deg,#5a3a2a 0%,#2c7f80 55%,#1a1c24 100%)"></div>
  <div class="video-bar"><span class="avatar"></span><span>Calculators and New Tools Coming Soon!</span></div>
  <div class="video-act" style="left:342px">◷<span>Watch later</span></div>
  <div class="video-act" style="left:417px">↪<span>Share</span></div>
</div>

<!-- CMA -->
<div class="abs cma-card"></div>
<div class="abs cma-inner">
  <h2 class="h-bold" style="margin-top:46px">Comparable And <span class="accent">CMA Report</span></h2>
  <p style="font-size:16px;line-height:25px;margin:22px auto 0;width:700px">Track real-time market trends, screen sold properties, pull comps, export data, and genera. Comprehensive CMA reports effortlessly.</p>
</div>
<div class="abs btn-outline">CMA Report
  <svg width="14" height="12" viewBox="0 0 14 12" fill="none" stroke="currentColor" stroke-width="1.5"><path d="M1 6h12M8 1l5 5-5 5"/></svg>
</div>

<!-- Calculators -->
<div class="abs calc-glow"></div>
<h2 class="abs h-bold" style="left:102px;top:2425px">Calculate Your <span class="accent">Numbers</span></h2>
<div class="abs calc-card" style="left:102px;top:2518px">
  <svg width="38" height="30" viewBox="0 0 38 30" fill="none" stroke="var(--navy)" stroke-width="1.6"><rect x="2" y="6" width="34" height="20" rx="2"/><circle cx="19" cy="16" r="6"/><path d="M19 12v8M6 10v12M32 10v12"/></svg>
  <span>Cash to Close</span>
</div>
<div class="abs calc-card" style="left:442px;top:2518px">
  <svg width="40" height="30" viewBox="0 0 40 30" fill="none" stroke="var(--navy)" stroke-width="1.6"><path d="M20 3v24M8 8h24M8 8l-5 10h10zM32 8l-5 10h10zM12 27h16"/></svg>
  <span>DSCR Calculator</span>
</div>
<div class="abs calc-card" style="left:102px;top:2681px">
  <svg width="36" height="34" viewBox="0 0 36 34" fill="none" stroke="var(--navy)" stroke-width="1.6"><rect x="10" y="8" width="22" height="24" rx="2"/><path d="M15 15h12M15 20h12M15 25h12"/><circle cx="9" cy="9" r="6"/><path d="M9 6v6"/></svg>
  <span>Filp Profit Estimator</span>
</div>
<div class="abs calc-card" style="left:442px;top:2681px">
  <svg width="36" height="36" viewBox="0 0 36 36" fill="none" stroke="var(--navy)" stroke-width="1.6"><circle cx="18" cy="18" r="15" stroke-dasharray="5 3"/><path d="M12 24v-6M18 24v-10M24 24v-8"/></svg>
  <span>Rehab Estimator</span>
</div>
<div class="abs calc-art" role="img" aria-label="Illustration of a man using a large orange calculator with gears"></div>

<!-- Achievements -->
<div class="abs ach-band"></div>
<div class="abs ach-box"></div>
<div class="abs ach-ring"></div>
<div class="abs medal" role="img" aria-label="Award medal"></div>
<div class="abs ach-title">Our Achievements</div>
<div class="abs stat" style="left:507px;top:2955px">
  <svg width="32" height="32" viewBox="0 0 32 32" fill="none" stroke="#fff" stroke-width="1.6"><circle cx="15" cy="17" r="12"/><circle cx="15" cy="17" r="7"/><circle cx="15" cy="17" r="2"/><path d="M15 17l12-12M22 5h5v5"/></svg>
  <div class="stat-num">305K</div><div class="stat-label">Lenders</div>
</div>
<div class="abs stat" style="left:697px;top:2955px">
  <svg width="32" height="32" viewBox="0 0 32 32" fill="none" stroke="#fff" stroke-width="1.6"><path d="M16 4a8 8 0 018 8c0 4-3 6-4 9h-8c-1-3-4-5-4-9a8 8 0 018-8zM12 25h8M13 29h6"/></svg>
  <div class="stat-num">782K</div><div class="stat-label">Investors</div>
</div>
<div class="abs stat" style="left:898px;top:2955px">
  <svg width="34" height="32" viewBox="0 0 34 32" fill="none" stroke="#fff" stroke-width="1.6"><circle cx="10" cy="7" r="3"/><circle cx="24" cy="7" r="3"/><circle cx="17" cy="5" r="3"/><path d="M3 24l8-9 6 5 6-5 8 9M10 26l7 4 7-4"/></svg>
  <div class="stat-num">67,23K</div><div class="stat-label">Loan Requests</div>
</div>

</body>
</html>
```